Zielgruppe
Scharf schiessen für Jedermann
Aufgabenstellung
Wir möchten unser Produkt auf einer A4 Seite in einem Eroitk Magazin präsentieren.
Es soll den Lesern Lust machen zu uns zu kommen und mit scharfen Waffen zu schiessen.
kernpunkte :
1. Berlin
2. Waffen
3. Event
4. Entertainment
Es daff keinen XXX Bezug haben.
Bilder Content darf von unser Webseite: www.zielwerk-beispiel.net genutzt werden.

```html
<!DOCTYPE html>
<html lang="de">
<head>
<meta charset="utf-8">
<title>Kernblitz – Schießen für jedermann</title>
<link rel="stylesheet" href="https://fonts.googleapis.com/css2?family=Carlito:ital,wght@1,700&family=Lato:wght@300;400&display=swap">
<style>
  :root {
    --sky-blue: #1c6598;
    --night: #000000;
    --text-white: #ffffff;
    --brand-blue: #9cc6ea;
    --silhouette: #2a2a2a;
  }
  html, body {
    margin: 0;
    padding: 0;
    overflow: hidden;
    background: var(--night);
  }
  .flyer {
    position: relative;
    width: 848px;
    height: 1200px;
    overflow: hidden;
    background: var(--night);
    font-family: "Lato", sans-serif;
    color: var(--text-white);
  }
  .hero {
    position: absolute;
    left: 0;
    top: 0;
    width: 848px;
    height: 728px;
    background: var(--sky-blue);
  }
  .brand {
    position: absolute;
    right: 60px;
    top: 92px;
    display: flex;
    align-items: center;
    gap: 14px;
  }
  .brand-dot {
    width: 34px;
    height: 34px;
    border-radius: 50%;
    background: var(--brand-blue);
  }
  .brand-name {
    font-family: "Lato", sans-serif;
    font-weight: 400;
    font-size: 52px;
    color: var(--brand-blue);
    letter-spacing: 1px;
  }
  .headline {
    position: absolute;
    left: 0;
    top: 258px;
    width: 848px;
    margin: 0;
    text-align: center;
    font-family: "Carlito", sans-serif;
    font-style: italic;
    font-weight: 700;
    font-size: 50px;
    letter-spacing: 0.5px;
  }
  .pistol-art {
    position: absolute;
    left: 128px;
    top: 368px;
    width: 180px;
    height: 134px;
    background: var(--silhouette);
    border-radius: 6px 6px 10px 18px;
  }
  .info {
    position: absolute;
    left: 326px;
    top: 370px;
    font-weight: 300;
  }
  .info-lead {
    margin: 0;
    font-size: 30px;
  }
  .info-url {
    margin: 8px 0 0;
    font-size: 36px;
  }
  .skyline-art {
    position: absolute;
    left: 0;
    top: 590px;
    width: 848px;
    height: 138px;
    background: linear-gradient(to bottom, rgba(0,0,0,0) 0%, rgba(0,0,0,0.85) 55%, var(--night) 100%);
  }
  .offer {
    position: absolute;
    left: 51px;
    top: 764px;
    width: 420px;
    font-size: 20px;
    line-height: 28px;
  }
  .offer p {
    margin: 0 0 28px;
  }
  .contact {
    position: absolute;
    left: 521px;
    top: 1030px;
    font-size: 20px;
    line-height: 38px;
  }
  .contact p {
    margin: 0;
  }
</style>
</head>
<body>
  <main class="flyer">
    <section class="hero">
      <div class="brand">
        <span class="brand-dot"></span>
        <span class="brand-name">Kernblitz</span>
      </div>
      <h1 class="headline">Schießen für jedermann!</h1>
      <div class="pistol-art" role="img" aria-label="Dunkle Silhouette einer Pistole"></div>
      <div class="info">
        <p class="info-lead">Weitere Infos unter</p>
        <p class="info-url">www.zielwerk-beispiel.net</p>
      </div>
      <div class="skyline-art" role="img" aria-label="Schwarze Silhouette der Berliner Skyline mit Fernsehturm und Brandenburger Tor"></div>
    </section>

    <section class="offer">
      <p>Bei uns haben Sie die Auswahl aus ver-<br>schiedenen Lang- und Kurzwaffen, sowie<br>verschiedenen Munitions- bzw, Kaliber-<br>arten.</p>
      <p>Von der handlichen 9mm Falkner-Pistole,<br>bekannt aus den Jack Stahl Filmen, über<br>den schweren 44er Magnum-Revolver aus<br>Kalter Harald, bis hin zu Schrotflinten und<br>Scharfschützengewehren.</p>
      <p>Hier ist für jeden Geschmack etwas dabei.</p>
    </section>

    <address class="contact" style="font-style: normal;">
      <p>Email: info@zielwerk-beispiel.net</p>
      <p>Telefon: 030 555 010 204</p>
    </address>
  </main>
</body>
</html>
```